Solar panel cleaning flyer design.

I'm looking for a flyer design for my new company called Brightfield Panel Works. We are a South Australian company that professionally clean residential and commercial solar panels. We generate leads by going door to door and need a flyer to hand out to our customers if they are interested in our service. As we are a new company we don't have anything particular in mind so be creative! Must include the company name and logo.

```html
<!DOCTYPE html>
<html lang="en">
<head>
<meta charset="utf-8">
<title>Brightfield Panel Works – Flyer</title>
<link href="https://fonts.googleapis.com/css2?family=Questrial&display=swap" rel="stylesheet">
<style>
  :root {
    --sky-light: #e9f3fb;
    --sky-blue: #4a94d6;
    --panel-navy: #1d3f9a;
    --band-blue: #0a7fc8;
    --lime: #a6ce39;
    --lime-bright: #d7e42a;
    --heading-blue: #1f5a8a;
    --brand-blue: #1b5fa8;
    --body-grey: #5a5a5a;
    --footer-green: #16924a;
    --roof-green: #2f9a3c;
    --wall-white: #f4f4f4;
    --rule-grey: #c9c9c9;
    --white: #ffffff;
  }
  * { margin: 0; padding: 0; box-sizing: border-box; }
  html, body { width: 850px; height: 1200px; overflow: hidden; background: var(--white); }
  body { font-family: "Questrial", "Century Gothic", sans-serif; }

  .flyer { position: relative; width: 850px; height: 1200px; overflow: hidden; background: var(--white); }

  .hero-photo {
    position: absolute; left: 0; top: 0; width: 850px; height: 484px;
    background: linear-gradient(160deg, var(--sky-light) 0%, #bcd9f1 30%, var(--sky-blue) 55%, var(--panel-navy) 100%);
  }
  .hero-band { position: absolute; left: 0; top: 360px; width: 850px; height: 124px; }

  .house-illustration {
    position: absolute; left: 30px; top: 232px; width: 320px; height: 306px;
    border-radius: 10px;
    background: linear-gradient(180deg, var(--roof-green) 0%, #5fb05a 40%, #dfe9dc 62%, var(--wall-white) 100%);
  }

  .hero-title {
    position: absolute; left: 38px; top: 44px;
    font-size: 29px; line-height: 34px; color: var(--heading-blue);
    text-transform: uppercase; font-weight: 400; letter-spacing: -0.2px;
  }

  .intro { position: absolute; left: 38px; top: 564px; width: 440px; }
  .intro-title { font-size: 29px; line-height: 34px; color: var(--lime); text-transform: uppercase; font-weight: 400; margin-bottom: 4px; letter-spacing: -0.2px; }
  .intro-text { font-size: 27px; line-height: 33.7px; color: var(--body-grey); }

  .services {
    position: absolute; left: 507px; top: 482px; width: 297px; height: 406px;
    background: var(--lime); border-radius: 0 0 32px 32px;
    padding: 24px 0 0 25px; color: var(--white);
  }
  .services-title { font-size: 29px; line-height: 34px; text-align: center; font-weight: 400; margin-bottom: 10px; padding-right: 22px; }
  .services-text { font-size: 27px; line-height: 33.6px; white-space: nowrap; }

  .brand { position: absolute; left: 505px; top: 906px; width: 310px; text-align: center; }
  .brand-mark { width: 80px; height: 80px; border-radius: 50%; background: var(--brand-blue); margin: 0 auto 16px; }
  .brand-name { font-size: 26px; color: var(--brand-blue); }

  .footer {
    position: absolute; left: 0; top: 1088px; width: 850px; height: 112px;
    background: var(--footer-green); border-top: 3px solid var(--rule-grey);
    color: var(--white); text-align: center;
  }
  .footer-label { font-size: 18px; line-height: 20px; margin-top: 11px; letter-spacing: 0.2px; }
  .footer-phone { font-size: 48px; line-height: 46px; margin-top: 2px; letter-spacing: 0.5px; }
  .footer-web { font-size: 21px; line-height: 22px; }
</style>
</head>
<body>
<main class="flyer">
  <div class="hero-photo" role="img" aria-label="Photo of rows of blue solar panels under a bright cloudy sky"></div>

  <svg class="hero-band" viewBox="0 0 850 124" preserveAspectRatio="none" aria-hidden="true">
    <path d="M0 40 C 200 130, 550 150, 850 20 L850 124 L0 124 Z" fill="var(--band-blue)"/>
    <path d="M340 62 C 520 95, 700 70, 850 20 L850 38 C 700 95, 520 105, 340 70 Z" fill="var(--lime)"/>
    <path d="M340 70 C 520 105, 700 95, 850 38 L850 48 C 700 100, 520 115, 340 80 Z" fill="var(--lime-bright)"/>
  </svg>

  <div class="house-illustration" role="img" aria-label="Illustration of a white house with a green roof and rooftop solar panels"></div>

  <h1 class="hero-title">Lorem ipsum dolor sit amet,<br>consectetur adipisicing elit, sed</h1>

  <section class="intro">
    <h2 class="intro-title">Lorem ipsum dolor sit amet,<br>consectetur adipisicing</h2>
    <p class="intro-text">Lorem ipsum dolor sit amet,<br>consectetur adipisicing elit, sed<br>do eiusmod tempor incididunt ut<br>labore et dolore magna aliqua. Ut<br>enim ad minim veniam, quis<br>nostrud exercitation ullamco<br>laboris nisi ut aliquip ex ea<br>commodo consequat. Duis aute<br>irure dolor in reprehenderit in<br>voluptate velit esse cillum dolore<br>eu fugiat nulla pariatur. Excepteur<br>sint occaecat cupidatat non</p>
  </section>

  <aside class="services">
    <h2 class="services-title">OUR SERVICES</h2>
    <p class="services-text">Lorem ipsum dolor sit<br>amet, consectetur<br>adipisicing elit, sed do<br>eiusmod tempor<br>incididunt ut labore et<br>dolore magna aliqua.<br>Ut enim ad minim<br>veniam, quis nostrud</p>
  </aside>

  <div class="brand">
    <div class="brand-mark" aria-hidden="true"></div>
    <p class="brand-name">Brightfield Panel Works</p>
  </div>

  <footer class="footer">
    <p class="footer-label">FOR MORE INFORMATION CALL</p>
    <p class="footer-phone">0412587306</p>
    <p class="footer-web">www.brightfieldpanels.com.au</p>
  </footer>
</main>
</body>
</html>
```